Web Design Project for Vantor Ridge Advisors, LP

We are looking for a new website for Vantor Ridge Advisors, LP an investment management (alternative investment) firm with offices in New York, NY and Seattle, WA. We are looking for designs utilizing gray, blue and white, corresponding with our logo. Our current website is www.vantorridgefund.example.

Some websites with the feel we are looking for:

http://brovikholdings.example/cgi-bin/index.pl
http://www.quillfieldpartners.example/

Target Market(s)

wealthy individuals and large investors

Industry/Entity Type

Investment

Requirements
Must have
• A couple/few page website, utilizing the below text & contact info and use one of the logos that are attached.

Text to be inlcuded:

Vantor Ridge Advisors, LP is a hedge fund manager responsible for a multi-strategy fund primarily implementing a long/short equity strategy and utilizing macro, credit, event driven and distressed strategies while maintaining a market neutral portfolio.

The Fund seeks to achieve absolute returns while minimizing risk with particular attention paid to preserving capital.

Contact information to be included:

East Coast:

417 Halberg Street #635
New York, NY 10029
Phone : +1 212.555.0147
Fax : +1 212.555.0193
contact@vantorridgefund.example

West Coast:

3847 Wexley Lane #508
Seattle, WA 98134
contact@vantorridgefund.example
Should not have
• anything too flashy

```html
<!DOCTYPE html>
<html lang="en">
<head>
<meta charset="utf-8">
<title>Contact — Vantor Ridge Advisors, LP</title>
<link href="https://fonts.googleapis.com/css2?family=Tinos:wght@400;700&display=swap" rel="stylesheet">
<style>
  :root {
    --navy: #2c4a73;
    --navy-dark: #233e63;
    --navy-light: #35557f;
    --ink: #4a4a4a;
    --muted: #7a7a7a;
    --rule: #cfcfcf;
    --page: #ffffff;
    --bubble: #f3f3f3;
    --bubble-dark: #e2e2e2;
    --photo-a: #c9d3dc;
    --photo-b: #eef1f4;
  }
  * { margin: 0; padding: 0; box-sizing: border-box; }
  html, body { width: 1200px; height: 872px; overflow: hidden; background: var(--page); }
  body { font-family: "Tinos", "Times New Roman", serif; color: var(--ink); position: relative; }

  .backdrop { position: absolute; inset: 0; width: 1200px; height: 872px; }

  .brand { position: absolute; left: 236px; top: 154px; font-size: 24px; color: var(--navy); letter-spacing: 0.5px; }
  .header-contact { position: absolute; left: 764px; top: 152px; font-size: 14px; line-height: 18px; color: var(--ink); white-space: nowrap; }

  .nav-band {
    position: absolute; left: 0; top: 199px; width: 1200px; height: 42px;
    background: linear-gradient(var(--navy-light), var(--navy-dark));
  }
  .nav-list { list-style: none; position: absolute; top: 0; left: 0; height: 42px; }
  .nav-list li { position: absolute; top: 13px; font-size: 13.5px; color: #fff; letter-spacing: 0.3px; white-space: nowrap; }
  .nav-list li.active::after {
    content: ""; position: absolute; left: 50%; bottom: -15px; margin-left: -4px;
    border: 4px solid transparent; border-bottom-color: #fff;
  }
  .search {
    position: absolute; left: 804px; top: 8px; width: 156px; height: 26px; background: #fff;
    font-size: 11.5px; color: var(--muted); padding: 6px 0 0 10px;
  }
  .search svg { position: absolute; right: 10px; top: 6px; }

  .portrait {
    position: absolute; left: 235px; top: 270px; width: 170px; height: 170px; border-radius: 50%;
    border: 5px solid #fff; box-shadow: 0 4px 10px rgba(0,0,0,0.18);
    background: radial-gradient(circle at 55% 40%, var(--photo-b), var(--photo-a));
  }

  .page-title { position: absolute; left: 426px; top: 263px; font-size: 23px; font-weight: 400; color: var(--navy); }
  .contact-panel {
    position: absolute; left: 430px; top: 304px; width: 389px; height: 267px;
    border-top: 1px solid var(--rule); border-right: 1px solid var(--rule);
  }
  .office { position: absolute; left: 0; font-size: 13.5px; line-height: 21px; font-style: normal; }
  .office strong { font-weight: 700; }
  .office-east { top: 14px; }
  .office-west { top: 88px; }
  .direct { position: absolute; left: 178px; top: 130px; font-size: 13.5px; line-height: 21px; font-style: normal; white-space: nowrap; }
  .send-button {
    position: absolute; left: 259px; top: 211px; width: 97px; height: 29px;
    background: var(--navy); color: #fff; font-size: 13px; font-weight: 700;
    text-align: center; line-height: 28px;
  }
  .send-button::after {
    content: ""; position: absolute; left: 50%; bottom: 0; margin-left: -4px;
    border: 4px solid transparent; border-bottom-color: #fff;
  }

  .footer-rule { position: absolute; left: 0; width: 1200px; height: 1px; background: var(--rule); }
  .footer {
    position: absolute; left: 235px; top: 571px; width: 740px; height: 47px;
    border: 1px solid var(--rule); background: #fff; font-size: 13.5px;
  }
  .copyright { position: absolute; left: 18px; top: 14px; }
  .copyright strong { color: var(--navy); }
  .footer-links { list-style: none; position: absolute; top: 14px; left: 0; }
  .footer-links li { position: absolute; white-space: nowrap; color: var(--muted); }
</style>
</head>
<body>
  <svg class="backdrop" viewBox="0 0 1200 872" aria-hidden="true">
    <defs>
      <filter id="soft" x="-20%" y="-20%" width="140%" height="140%"><feGaussianBlur stdDeviation="6"/></filter>
    </defs>
    <circle cx="135" cy="-60" r="185" fill="var(--bubble)"/>
    <circle cx="457" cy="134" r="36" fill="var(--bubble)"/>
    <circle cx="494" cy="113" r="23" fill="var(--bubble)"/>
    <circle cx="1185" cy="300" r="215" fill="var(--bubble)" filter="url(#soft)"/>
    <circle cx="801" cy="178" r="11" fill="var(--bubble)"/>
    <circle cx="812" cy="194" r="12" fill="var(--bubble)"/>
    <circle cx="100" cy="680" r="205" fill="var(--bubble-dark)" filter="url(#soft)"/>
  </svg>

  <header>
    <div class="brand">Vantor Ridge Advisors, LP</div>
    <div class="header-contact">Phone : +1 212.555.0147<br>contact@vantorridgefund.example</div>
  </header>

  <nav class="nav-band">
    <ul class="nav-list">
      <li style="left:238px">HOME</li>
      <li style="left:316px">ABOUT VRA</li>
      <li style="left:426px">TEAM</li>
      <li style="left:502px">NEWS</li>
      <li style="left:579px">GALLERY</li>
      <li class="active" style="left:680px">CONTACT</li>
    </ul>
    <div class="search">Search your phrase...
      <svg width="14" height="14" viewBox="0 0 14 14"><circle cx="5.5" cy="5.5" r="4.3" fill="none" stroke="#555" stroke-width="2"/><line x1="8.6" y1="8.6" x2="12.5" y2="12.5" stroke="#555" stroke-width="2.4" stroke-linecap="round"/></svg>
    </div>
  </nav>

  <main>
    <div class="portrait" role="img" aria-label="Photo of a smiling customer service representative wearing a headset"></div>
    <h1 class="page-title">Contact</h1>
    <section class="contact-panel">
      <address class="office office-east"><strong>East Coast:</strong><br>417 Halberg Street #635<br>New York, NY 10029</address>
      <address class="office office-west"><strong>West Coast:</strong><br>3847 Wexley Lane #508<br>Seattle, WA 98134</address>
      <address class="direct">Phone : +1 212.555.0147<br>Fax : +1 212.555.0193<br>contact@vantorridgefund.example</address>
      <div class="send-button">send message</div>
    </section>
  </main>

  <div class="footer-rule" style="top:571px"></div>
  <div class="footer-rule" style="top:617px"></div>
  <footer class="footer">
    <p class="copyright">Copyright by <strong>VANTOR RIDGE</strong>. All rights reserved.</p>
    <ul class="footer-links">
      <li style="left:530px">Home</li>
      <li style="left:579px">Site map</li>
      <li style="left:644px">Privacy Policy</li>
    </ul>
  </footer>
</body>
</html>
```